Recycling Poster

HI
Looking for clean and clear new recycling posters for plastic bottles, glass bottles , and aluminium cans we have attached an industry sample we are looking for a new clean look and feel
Colour scheme light blue , yellow and font in black
size a2

Target Market(s)

consumer

Industry/Entity Type

Industry

Font styles to use
Sans Serif

Colors
fbee3e
33a6d7
acd036
faa54b

Requirements
Must have
• the logo *quillora I have just attached
Should not have
• do not include the "do the right thing text or tidy horizon logo and bin
• do not use crushed containers

```html
<!DOCTYPE html>
<html lang="en">
<head>
<meta charset="utf-8">
<title>Recycle Here – Quillora</title>
<link rel="stylesheet" href="https://fonts.googleapis.com/css2?family=Lato:ital,wght@0,400;0,700;0,900;1,900&family=Permanent+Marker&display=swap">
<style>
  :root {
    --sky: #33a6d7;
    --sky-deep: #1d7fb4;
    --sky-light: #6cc6ec;
    --sun: #fbee3e;
    --sun-deep: #f3c81a;
    --leaf: #acd036;
    --tangerine: #faa54b;
    --ink: #111111;
    --paper: #ffffff;
  }
  * { margin: 0; padding: 0; box-sizing: border-box; }
  html, body { width: 889px; height: 1200px; overflow: hidden; background: #e9e9e9; }
  .poster {
    position: relative;
    width: 889px;
    height: 1200px;
    overflow: hidden;
    font-family: "Lato", Arial, sans-serif;
    background: var(--sky);
  }
  .header-band {
    position: absolute; inset: 0 0 auto 0; height: 260px;
    background: linear-gradient(180deg, var(--sky-light) 0%, var(--sky) 55%, var(--sky-deep) 100%);
  }
  .headline {
    position: absolute; top: 58px; left: 0; right: 0;
    text-align: center;
    font-weight: 900;
    line-height: 1;
    letter-spacing: 1px;
    text-transform: uppercase;
  }
  .headline .word-recycle { color: var(--paper); -webkit-text-stroke: 3px #0e4f73; font-size: 86px; }
  .headline .word-here { color: var(--sun); -webkit-text-stroke: 3px #0e4f73; font-size: 120px; }
  .feature-panel {
    position: absolute; left: 0; right: 0; top: 200px; height: 700px;
  }
  .feature-panel svg { position: absolute; inset: 0; width: 100%; height: 100%; }
  .product-photo {
    position: absolute; left: 90px; top: 280px; width: 710px; height: 380px;
    border-radius: 14px;
    background: radial-gradient(ellipse at 50% 45%, #eaf4f8 0%, #b9d6e3 45%, #8fb0bf 75%, rgba(143,176,191,0.2) 100%);
  }
  .accepted-items {
    position: absolute; left: 0; right: 0; top: 680px;
    text-align: center; color: var(--ink);
  }
  .accepted-items .line-bottles { font-weight: 900; font-style: italic; font-size: 60px; letter-spacing: -1px; }
  .accepted-items .line-cans { font-weight: 400; font-size: 62px; text-transform: uppercase; letter-spacing: 1px; margin-top: 2px; }
  .brand {
    position: absolute; left: 60px; top: 1000px;
  }
  .brand-name { font-weight: 900; font-size: 84px; color: var(--paper); line-height: 1; }
  .rules-tag {
    position: absolute; left: 560px; top: 985px; width: 290px; height: 130px;
    background: var(--tangerine);
    transform: rotate(-10deg);
    display: flex; flex-direction: column; justify-content: center; align-items: center;
    font-family: "Permanent Marker", "Lato", sans-serif;
    font-size: 30px; line-height: 1.2; color: #5a2a0a;
    box-shadow: 0 3px 8px rgba(0,0,0,0.25);
  }
</style>
</head>
<body>
<main class="poster">
  <div class="header-band"></div>
  <h1 class="headline"><span class="word-recycle">Recycle</span> <span class="word-here">Here</span></h1>

  <section class="feature-panel">
    <svg viewBox="0 0 889 700" preserveAspectRatio="none" aria-hidden="true">
      <defs>
        <radialGradient id="sunGlow" cx="50%" cy="40%" r="70%">
          <stop offset="0%" stop-color="#fff8a6"/>
          <stop offset="55%" stop-color="#fbee3e"/>
          <stop offset="100%" stop-color="#f3c81a"/>
        </radialGradient>
      </defs>
      <path fill="#ffffff" d="M0 22 L40 8 L85 26 L130 4 L180 20 L235 2 L290 24 L345 6 L400 22 L455 0 L510 18 L565 4 L620 24 L675 6 L730 20 L785 2 L840 22 L889 10 L889 692 L845 678 L795 698 L740 680 L690 700 L635 682 L580 698 L525 680 L470 700 L415 682 L360 698 L305 678 L250 698 L195 680 L140 700 L85 682 L35 698 L0 684 Z"/>
      <path fill="url(#sunGlow)" d="M0 32 L45 18 L90 36 L135 14 L185 30 L240 12 L295 34 L350 16 L405 32 L460 10 L515 28 L570 14 L625 34 L680 16 L735 30 L790 12 L845 32 L889 20 L889 682 L845 668 L795 688 L740 670 L690 690 L635 672 L580 688 L525 670 L470 690 L415 672 L360 688 L305 668 L250 688 L195 670 L140 690 L85 672 L35 688 L0 674 Z"/>
    </svg>
  </section>

  <div class="product-photo" role="img" aria-label="Photo of a blue glass bottle, two aluminium cans and a clear plastic water bottle"></div>

  <div class="accepted-items">
    <p class="line-bottles">Plastic bottles, glass bottles</p>
    <p class="line-cans">and Aluminium cans</p>
  </div>

  <div class="brand">
    <span class="brand-name">quillora</span>
  </div>

  <div class="rules-tag">
    <span>NO FOOD SCRAPS</span>
    <span>NO PLASTIC BAG</span>
  </div>
</main>
</body>
</html>
```